Business Card Design

We need a business card designed which uses our logo and looks really good. The company is called Veltramor482. We help e-commerce companies reduce cart abandonment by rescuing the sale through our innovative technology.

Our corporate colors are red, black and white.

I have attached our AI file for the logo as well.

Additional information for the business card:

Name: Marcus Delby
Title: President/CTO
Phone: 1-877-VELT-482
Website: www.veltramor482.com
Email: marcus@veltramor482.com

Tag line: Winning Back Every Checkout

Industry/Entity Type

E-Commerce

```html
<!DOCTYPE html>
<html lang="en">
<head>
<meta charset="utf-8">
<title>Veltramor482 Business Card Concepts</title>
<link rel="stylesheet" href="https://fonts.googleapis.com/css2?family=Open+Sans:wght@400;600&family=Marcellus+SC&family=Courgette&display=swap">
<style>
  :root {
    --stage: #9a9f99;
    --paper: #ffffff;
    --brand-red: #ed1c24;
    --brand-black: #000000;
    --ink: #111111;
    --rule-grey: #8a8a8a;
    --logo-ink: #1a1a1a;
  }
  * { margin: 0; padding: 0; box-sizing: border-box; }
  html, body { width: 1200px; height: 1000px; overflow: hidden; }
  body { background: var(--stage); position: relative; font-family: "Open Sans", Arial, sans-serif; }

  .card { position: absolute; width: 548px; height: 320px; background: var(--paper); overflow: hidden; }
  .card--a { left: 32px; top: 60px; }
  .card--b { left: 610px; top: 62px; }
  .card--c { left: 34px; top: 610px; width: 545px; }
  .card--d { left: 613px; top: 610px; width: 545px; }

  .wordmark { position: absolute; display: flex; align-items: center; gap: 8px;
    font-family: "Open Sans", Arial, sans-serif; font-weight: 400; color: var(--logo-ink); letter-spacing: -0.5px; white-space: nowrap; }
  .wordmark__square { width: 0.55em; height: 0.55em; background: var(--brand-red); display: inline-block; }

  /* Classic band layout */
  .classic .wordmark { left: 0; right: 0; top: 32px; justify-content: center; font-size: 38px; line-height: 1; }
  .classic .tagline { position: absolute; left: 90px; width: 356px; top: 84px; text-align: center;
    font-family: "Courgette", cursive; color: var(--brand-red); font-size: 19px; padding-bottom: 4px;
    border-bottom: 2px solid var(--rule-grey); white-space: nowrap; }
  .classic .site { position: absolute; left: 0; right: 0; top: 146px; text-align: center; font-size: 15px; color: var(--ink); }
  .classic .band { position: absolute; left: 0; right: 0; top: 203px; bottom: 0; color: #fff; }
  .band--red { background: var(--brand-red); }
  .band--black { background: var(--brand-black); }
  .classic .person { position: absolute; left: 20px; width: 236px; top: 26px; text-align: center; }
  .classic .person__name { font-family: "Marcellus SC", Georgia, serif; font-size: 22px; line-height: 1.1; }
  .classic .person__title { font-size: 14px; margin-top: 3px; }
  .classic .divider { position: absolute; left: 259px; top: 10px; height: 82px; width: 1.5px; background: #fff; }
  .classic .contact { position: absolute; left: 282px; top: 20px; font-size: 16px; white-space: nowrap; }
  .classic .contact__row { display: flex; align-items: center; gap: 6px; height: 26px; margin-bottom: 9px; }
  .classic .icon { width: 22px; height: 22px; }

  /* Angled header layout */
  .angled .wordmark { left: 32px; top: 44px; font-size: 30px; line-height: 1; }
  .angled .header-band { position: absolute; left: 0; top: 0; width: 545px; height: 110px; }
  .angled .tagline-rule { position: absolute; left: 0; right: 0; top: 117px; height: 1px; background: var(--rule-grey); }
  .angled .tagline { position: absolute; right: 20px; top: 106px; background: var(--paper); padding: 0 4px; font-size: 16px; white-space: nowrap; }
  .tagline--red { color: var(--brand-red); }
  .tagline--ink { color: var(--ink); }
  .angled .person { position: absolute; left: 30px; width: 244px; top: 225px; text-align: center; }
  .angled .person__name { font-family: "Marcellus SC", Georgia, serif; font-size: 22px; color: var(--brand-red); line-height: 1.1; }
  .angled .person__title { font-size: 12px; color: var(--ink); margin-top: 4px; }
  .angled .divider { position: absolute; left: 256px; top: 215px; height: 66px; width: 1.5px; background: var(--brand-red); }
  .angled .contact { position: absolute; left: 276px; top: 214px; font-size: 12px; color: var(--ink); white-space: nowrap; }
  .angled .contact__row { display: flex; align-items: center; gap: 5px; height: 20px; margin-bottom: 5px; }
  .angled .contact__row--site { padding-left: 28px; }
  .angled .icon { width: 19px; height: 19px; }
</style>
</head>
<body>

<svg width="0" height="0" style="position:absolute">
  <defs>
    <symbol id="icon-phone" viewBox="0 0 24 24">
      <circle cx="12" cy="12" r="10.5" fill="none" stroke="currentColor" stroke-width="1.6"/>
      <path d="M8.6 6.5l1.8 0 1 2.8-1.3 1c.6 1.5 1.7 2.6 3.2 3.2l1-1.3 2.8 1v1.8c0 .6-.5 1-1.1 1-4.8-.3-8.6-4.1-8.9-8.9 0-.6.4-1.1 1-1.1z" fill="currentColor"/>
    </symbol>
    <symbol id="icon-at" viewBox="0 0 24 24">
      <circle cx="12" cy="12" r="10.5" fill="none" stroke="currentColor" stroke-width="1.6"/>
      <text x="12" y="16.3" text-anchor="middle" font-family="Open Sans, Arial, sans-serif" font-size="13" font-weight="600" fill="currentColor">@</text>
    </symbol>
  </defs>
</svg>

<section class="card card--a classic">
  <div class="wordmark">Veltramor482<span class="wordmark__square"></span></div>
  <p class="tagline">Winning Back Every Checkout</p>
  <p class="site">www.veltramor482.com</p>
  <div class="band band--red">
    <div class="person"><p class="person__name">Marcus Delby</p><p class="person__title">President/CTO</p></div>
    <div class="divider"></div>
    <div class="contact">
      <p class="contact__row"><svg class="icon"><use href="#icon-phone"/></svg>1-877-VELT-482</p>
      <p class="contact__row"><svg class="icon"><use href="#icon-at"/></svg>marcus@veltramor482.com</p>
    </div>
  </div>
</section>

<section class="card card--b classic">
  <div class="wordmark">Veltramor482<span class="wordmark__square"></span></div>
  <p class="tagline">Winning Back Every Checkout</p>
  <p class="site">www.veltramor482.com</p>
  <div class="band band--black">
    <div class="person"><p class="person__name">Marcus Delby</p><p class="person__title">President/CTO</p></div>
    <div class="divider"></div>
    <div class="contact">
      <p class="contact__row"><svg class="icon"><use href="#icon-phone"/></svg>1-877-VELT-482</p>
      <p class="contact__row"><svg class="icon"><use href="#icon-at"/></svg>marcus@veltramor482.com</p>
    </div>
  </div>
</section>

<section class="card card--c angled">
  <svg class="header-band" viewBox="0 0 545 110"><polygon points="0,83 336,83 390,52 545,52 545,102 0,102" fill="var(--brand-black)"/></svg>
  <div class="wordmark">Veltramor482<span class="wordmark__square"></span></div>
  <div class="tagline-rule"></div>
  <p class="tagline tagline--red">Winning Back Every Checkout</p>
  <div class="person"><p class="person__name">Marcus Delby</p><p class="person__title">President/CTO</p></div>
  <div class="divider"></div>
  <div class="contact">
    <p class="contact__row"><svg class="icon"><use href="#icon-phone"/></svg>1-877-VELT-482</p>
    <p class="contact__row"><svg class="icon"><use href="#icon-at"/></svg>marcus@veltramor482.com</p>
    <p class="contact__row contact__row--site">www.veltramor482.com</p>
  </div>
</section>

<section class="card card--d angled">
  <svg class="header-band" viewBox="0 0 545 110"><polygon points="0,83 336,83 390,52 545,52 545,102 0,102" fill="var(--brand-red)"/></svg>
  <div class="wordmark">Veltramor482<span class="wordmark__square"></span></div>
  <div class="tagline-rule"></div>
  <p class="tagline tagline--ink">Winning Back Every Checkout</p>
  <div class="person"><p class="person__name">Marcus Delby</p><p class="person__title">President/CTO</p></div>
  <div class="divider"></div>
  <div class="contact">
    <p class="contact__row"><svg class="icon"><use href="#icon-phone"/></svg>1-877-VELT-482</p>
    <p class="contact__row"><svg class="icon"><use href="#icon-at"/></svg>marcus@veltramor482.com</p>
    <p class="contact__row contact__row--site">www.veltramor482.com</p>
  </div>
</section>

</body>
</html>
```